Buch-/eBook-Cover für Anti-Stress-Adventskalender
Zielgruppe
Wir sind als Selfpublisher vorwiegend bei Luvora BKP aktiv und veröffentlichen Taschenbücher im Bereich Sachbücher, Ratgeber und Kinderbücher. Die Zielgruppe ist bei diesem Projekt schwieriger zu bestimmten, aber wird vsl. im Bereich der jungen Erwachsenen liegen und tendenziell eher im weiblichen Publikum.
Aufgabenstellung
Das Design sollte ein individuell auf das Projekt und auf die Zielgruppe abgestimmtes Konzept verfolgen, welches auf Luvora in die Augen sticht und Besteller Potential hat. Es sollte sich an bereits vorhanden Bestsellern in der jeweiligen Nische orientieren und dabei trotzdem die eigene Idee verdeutlichen. Der Sarkasmus und Humor des Buches und des Haupttitels sollte aus dem Cover hervorgehen.
Der Haupttitel: 17 Arten, die Rentierherde nicht zu verlieren
Der Nebentitel: Dein lustiger Anti-Stress Adventskalender mit außergewöhnlichen Witzen, Rätseln und kreativen Aufgaben.
Autor: Jan Wolters
Die Maße des Taschenbuchs werden wie folgt sein: 15.24 x 0.64 x 22.86 cm

```html
<!DOCTYPE html>
<html lang="de">
<head>
<meta charset="utf-8">
<title>17 Arten, die Rentierherde nicht zu verlieren – Cover</title>
<link rel="stylesheet" href="https://fonts.googleapis.com/css2?family=Luckiest+Guy&family=Fredoka:wght@600&display=swap">
<style>
  :root {
    --backdrop: #c6c6c6;
    --kraft: #dccfa6;
    --kraft-shadow: #b9ab82;
    --christmas-red: #e2202a;
    --pine-green: #1f5a33;
    --snow: #ffffff;
    --santa-red: #d3242a;
    --santa-dark: #9e1b20;
  }
  * { margin: 0; padding: 0; box-sizing: border-box; }
  html, body {
    width: 1200px; height: 2317px; overflow: hidden;
    background: var(--backdrop);
  }
  .cover {
    position: absolute; left: 50px; top: 334px;
    width: 1100px; height: 1648px;
    background: var(--kraft);
    overflow: hidden;
    box-shadow: 0 6px 18px rgba(0,0,0,.18);
  }
  .layer { position: absolute; inset: 0; }
  .display {
    font-family: "Luckiest Guy", "Arial Black", sans-serif;
    font-weight: 400;
    line-height: 1;
    white-space: nowrap;
  }
  .title-number {
    position: absolute; left: 50px; top: 60px;
    width: 420px; text-align: center;
    font-size: 300px;
    color: var(--christmas-red);
    -webkit-text-stroke: 14px var(--snow);
    paint-order: stroke fill;
    text-shadow: 10px 12px 0 var(--kraft-shadow);
  }
  .title-word {
    position: absolute; left: 470px; top: 170px;
    width: 600px; text-align: center;
    font-size: 150px;
    color: var(--pine-green);
    -webkit-text-stroke: 12px var(--snow);
    paint-order: stroke fill;
    text-shadow: 8px 10px 0 var(--kraft-shadow);
  }
  .title-band {
    position: absolute; left: 25px; top: 395px;
    width: 1060px; height: 330px;
    background: var(--snow);
    transform: rotate(-2deg);
    padding: 40px 30px 0;
  }
  .title-line { color: var(--pine-green); font-size: 76px; }
  .title-row {
    display: flex; align-items: center; gap: 28px;
    margin-top: 50px;
  }
  .title-highlight {
    padding: 18px 22px 8px;
    background: var(--christmas-red);
    color: var(--snow);
    font-size: 90px;
  }
  .title-row .title-line { font-size: 70px; }
  .subtitle {
    position: absolute; left: 540px; top: 790px; width: 520px;
    font-family: "Fredoka", "Arial", sans-serif;
    font-weight: 600;
    font-size: 32px; line-height: 1.2;
    text-transform: uppercase; text-align: center;
    color: var(--pine-green);
  }
  .santa-illustration {
    position: absolute; left: 0; top: 820px;
    width: 500px; height: 828px;
    border-radius: 0 260px 0 0;
    background: linear-gradient(165deg, var(--santa-red) 0%, #f0e4dc 40%, var(--santa-red) 68%, var(--santa-dark) 100%);
  }
  .village-scene {
    position: absolute; left: 600px; top: 1060px;
    width: 500px; height: 220px;
    background: linear-gradient(180deg, rgba(255,255,255,0) 0%, rgba(255,255,255,.45) 100%);
  }
  .author {
    position: absolute; left: 560px; top: 1505px; width: 500px;
    text-align: right;
    font-size: 64px; letter-spacing: 3px;
    color: var(--christmas-red);
  }
</style>
</head>
<body>
  <main class="cover">
    <svg class="layer" width="1100" height="1648" viewBox="0 0 1100 1648" aria-hidden="true">
      <path class="snow-hill" d="M480 1330 C 680 1210, 900 1210, 1100 1240 L1100 1648 L480 1648 Z" fill="var(--snow)"/>
    </svg>

    <div class="village-scene" role="img" aria-label="Verschneite Winterlandschaft mit Häusern und Tannen in weißen Linien"></div>

    <div class="title-number display">17</div>
    <div class="title-word display">ARTEN</div>

    <div class="title-band">
      <div class="title-line display">DIE RENTIERHERDE</div>
      <div class="title-row">
        <span class="title-highlight display">NICHT</span>
        <span class="title-line display">ZU VERLIEREN</span>
      </div>
    </div>

    <svg class="layer" width="1100" height="1648" viewBox="0 0 1100 1648" aria-hidden="true">
      <path d="M640 735 C 620 800, 540 745, 480 775 C 455 790, 440 798, 420 800" fill="none" stroke="var(--christmas-red)" stroke-width="8" stroke-linecap="round"/>
      <path d="M440 778 L415 801 L445 815" fill="none" stroke="var(--christmas-red)" stroke-width="8" stroke-linecap="round" stroke-linejoin="round"/>
    </svg>

    <p class="subtitle">Dein lustiger Anti-Stress Adventskalender mit außergewöhnlichen Witzen, Rätseln und kreativen Aufgaben.</p>

    <div class="santa-illustration" role="img" aria-label="Comic-Weihnachtsmann in rotem Mantel mit grünem Handschuh, der einem Schneeball ausweicht"></div>

    <div class="author display">Jan Wolters</div>
  </main>
</body>
</html>
```